Create a Brochure Design for Harlow Senior Living

Harlow Senior Living is a subsidiary of the Harlow Care Group. This brochure is specifically for the Harlow Senior Living company and brand. Create a 3 panel, front and back, tri-fold brochure. This brochure will be a way to introduce our senior living care home to the community, prospective, clients, and various referral partners. It is modern and state of the art home. Like the home, the brochure must be eye catching, unique in its deliverables (as it doesn’t feel like a care facility) and demonstrate both attention to detail and comfort. Our organization is sophisticated and built around warmth, care and individualized personal attention. The most important aspect of this design is to focus on creating a nurturing, warm, and inviting feel where you would want to put your own loved ones in our care home.
I am open to the creativity of the designer to develop something based on the above criteria; however I would like the design to work well with the existing collateral material. What I mean by that is that while I want everything to have its own personality and stand out as its own brand representative, I still need to be able to tell that the overall design concept stays stylistically inside of the same ‘family’ of existing designed material. Because of this, below I would like for the designer to pull inspiration from the link to our website (Located below) as well as from the attachment of our recently refreshed business cards (Attached). This should allow each design to be unique and creative, while still staying inside of a framework and the feel/style that I am looking for.
Finally, I want all the designers to understand that this brochure design is for a facility where we are responsible to provide care for active, positive, and happy seniors/elders. We have care professionals and staff on-site to provide 24x7, around the clock, care to the elders and geriatric residents as it is needed and required. The photos that are used must represent aging gracefully and with elegance.
Target Market(s)
Seniors(50+), Caring Family Members, Social Workers, Physicians, Hospitals
Industry/Entity Type
Business
Requirements
Must have
- • The company logo must be included.
Nice to have
- Attached you will find a sampling of images related to the long term care industry. Please feel free to use your own images as you see fit. The interior care home pictures are of our actual facility and should be incorporated into the brochure and your design.
Company Information
• Look under the Harlow Senior Living tab at
www.harlowcaregroup.example.

```html
<!DOCTYPE html>
<html lang="en">
<head>
<meta charset="utf-8">
<title>Harlow Senior Living – Tri-fold Brochure</title>
<link href="https://fonts.googleapis.com/css2?family=Crimson+Text:wght@400;600;700&family=Source+Sans+3:wght@400;600&display=swap" rel="stylesheet">
<style>
  :root{
    --teal-light:#98d3cf;
    --teal-mid:#7fbab7;
    --teal-dark:#67999a;
    --teal-deep:#4f8f8d;
    --teal-text:#4a8f8c;
    --ink:#2c2c2c;
    --grey:#9a9a9a;
    --white:#ffffff;
    --serif:"Crimson Text", Georgia, serif;
    --sans:"Source Sans 3", Arial, sans-serif;
  }
  *{box-sizing:border-box;margin:0;padding:0}
  html,body{width:852px;height:1200px;overflow:hidden;background:var(--white)}
  body{position:relative;font-family:var(--serif);color:var(--ink)}

  .sheet{position:absolute;background:var(--white);box-shadow:0 2px 6px rgba(0,0,0,.25)}
  .sheet--outside{left:40px;top:62px;width:792px;height:613px}
  .sheet--inside{left:193px;top:705px;width:639px;height:493px}
  .panel{position:absolute;top:0;height:100%}

  /* outside */
  .panel--gallery{left:0;width:264px}
  .panel--gallery svg{display:block}
  .panel--contact{left:264px;width:264px;background:var(--teal-light);color:var(--white);text-align:center;font-family:var(--sans);font-size:11px;line-height:15px}
  .brand-mark{font-family:var(--serif);font-weight:600;display:flex;align-items:center;justify-content:center;gap:7px}
  .brand-mark__square{display:inline-block;background:currentColor}
  .panel--contact .brand-mark{position:absolute;top:200px;left:0;width:100%;font-size:21px;color:var(--white)}
  .panel--contact .brand-mark__square{width:12px;height:12px}
  .contact-block{position:absolute;left:0;width:100%}
  .panel--cover{left:528px;width:264px;background:var(--white)}
  .panel--cover .brand-mark{position:absolute;top:150px;left:0;width:100%;flex-direction:column;gap:10px;font-size:32px;line-height:32px;color:var(--teal-text)}
  .panel--cover .brand-mark__square{width:26px;height:26px}
  .tagline{position:absolute;top:262px;left:0;width:100%;text-align:center;font-family:var(--serif);font-weight:600;font-size:15px;line-height:19px;color:var(--grey)}
  .cover-photo{position:absolute;left:0;top:361px;width:264px;height:252px;background:linear-gradient(160deg,#8a6a4a 0%,#c29a6e 45%,#a57a52 70%,#6b4a2e 100%)}
  .welcome-band{position:absolute;left:0;top:421px;width:264px;height:62px;background:rgba(103,160,158,.78)}
  .welcome{position:absolute;left:60px;top:423px;color:var(--white);font-weight:700}
  .welcome__small{position:absolute;left:45px;top:0;font-size:16px;line-height:18px}
  .welcome__big{display:block;margin-top:6px;font-size:41px;line-height:44px}
  .cover-call{position:absolute;left:0;width:264px;top:574px;text-align:center;color:var(--white);font-weight:700;font-size:21px}

  /* inside */
  .column{position:absolute;top:0;height:100%;padding:20px 18px 0}
  .column--about{left:0;width:212px}
  .column--services{left:212px;width:213px;background:var(--teal-dark);color:var(--white);overflow:hidden}
  .column--fees{left:425px;width:214px}
  .column-title{font-size:21px;line-height:26px;font-weight:700;color:var(--teal-text)}
  .column--about .column-title{padding-bottom:3px;border-bottom:1px dotted #888}
  .column--services .column-title{color:var(--white);padding-bottom:3px;border-bottom:1px dotted rgba(255,255,255,.7)}
  .body-copy{font-size:9.6px;line-height:11.7px}
  .body-copy p+p{margin-top:11.7px}
  .column--about .body-copy{margin-top:10px}
  .column--services .body-copy{position:relative;z-index:1;margin-top:14px}
  .photo{position:relative;overflow:hidden}
  .photo__caption{position:absolute;left:0;bottom:0;padding:2px 8px 3px 8px;background:rgba(103,160,158,.82);color:var(--white);font-weight:700;line-height:1}
  .photo__caption small{display:block;font-size:13px;line-height:14px}
  .photo__caption span{display:block;font-size:32px;line-height:30px}
  .photo--life{margin:16px -8px 0;height:123px;background:linear-gradient(120deg,#c9d8e0 0%,#e8e2d8 40%,#d9c4ae 70%,#f2ede6 100%)}
  .column--about .body-copy.second{margin-top:17px}
  .services-swoosh{position:absolute;left:0;bottom:0;width:213px;height:170px}
  .column--fees .column-title{font-size:15px;line-height:20px;text-align:center;padding-top:4px}
  .fee-box{margin:8px -4px 0;background:var(--teal-mid);color:var(--white);font-family:var(--sans);font-size:7.2px;line-height:11.6px;letter-spacing:.09em;text-transform:uppercase;text-align:center;padding:5px 0 6px;list-style:none;font-weight:600}
  .care-heading{margin-top:10px;font-size:10px;font-weight:700;color:var(--teal-text)}
  .care-text{font-size:9.6px;line-height:11.7px}
  .photo--family{margin:13px -8px 0;height:123px;background:linear-gradient(110deg,#a89890 0%,#d9cfc6 45%,#eef0f0 75%,#cfd9dc 100%)}
</style>
</head>
<body>

<section class="sheet sheet--outside">
  <div class="panel panel--gallery">
    <svg width="264" height="613" viewBox="0 0 264 613">
      <defs>
        <clipPath id="gallery-shape">
          <path d="M0,150 C60,80 150,38 264,22 L264,548 C170,565 75,585 0,600 Z"/>
        </clipPath>
        <linearGradient id="living-tone" x1="0" y1="0" x2="1" y2="1">
          <stop offset="0" stop-color="#6b4c34"/><stop offset=".5" stop-color="#a7876a"/><stop offset="1" stop-color="#7d6a58"/>
        </linearGradient>
        <linearGradient id="bath-tone" x1="0" y1="0" x2="1" y2="1">
          <stop offset="0" stop-color="#d8d0c4"/><stop offset=".55" stop-color="#ece6dc"/><stop offset="1" stop-color="#a9764a"/>
        </linearGradient>
        <linearGradient id="bed-tone" x1="0" y1="0" x2="1" y2="1">
          <stop offset="0" stop-color="#e6d8a8"/><stop offset=".5" stop-color="#b89a78"/><stop offset="1" stop-color="#4a3a2e"/>
        </linearGradient>
      </defs>
      <rect width="264" height="613" fill="var(--teal-light)"/>
      <path d="M0,128 C60,55 150,18 264,8 L264,22 C150,38 60,80 0,150 Z" fill="var(--teal-dark)"/>
      <path d="M0,600 C75,585 170,565 264,548 L264,572 C170,590 80,608 0,613 Z" fill="var(--teal-dark)"/>
      <g clip-path="url(#gallery-shape)">
        <rect x="0" y="0" width="264" height="222" fill="url(#living-tone)" role="img" aria-label="Photo of the furnished living room with sofa"/>
        <rect x="0" y="224" width="264" height="173" fill="url(#bath-tone)" role="img" aria-label="Photo of a private accessible bathroom"/>
        <rect x="0" y="399" width="264" height="214" fill="url(#bed-tone)" role="img" aria-label="Photo of a private bedroom with patio door"/>
      </g>
    </svg>
  </div>

  <div class="panel panel--contact">
    <div class="brand-mark"><span class="brand-mark__square"></span>Harlow Senior Living</div>
    <div class="contact-block" style="top:420px">
      Harlow Senior Living is located at:<br>
      214 Coral Bay Drive<br>
      Seaview, HI 96700
    </div>
    <div class="contact-block" style="top:479px">
      Please direct all mail to:<br>
      PO Box 4170<br>
      Harbor City, HI 96800<br>
      Tel 808-555-0142<br>
      Fax 808-555-0187
    </div>
    <div class="contact-block" style="top:564px">E-mail us at info@harlowcare.example</div>
  </div>

  <div class="panel panel--cover">
    <div class="brand-mark"><span class="brand-mark__square"></span>Harlow<br>Senior Living</div>
    <p class="tagline">Quality Care.<br>Enrich Your Lifestyle.</p>
    <div class="cover-photo" role="img" aria-label="Photo of a sunny bedroom corner with bench and curtains"></div>
    <div class="welcome-band"></div>
    <div class="welcome"><span class="welcome__small">Welcome</span><span class="welcome__big">Home</span></div>
    <p class="cover-call">Call 808-555-0142</p>
  </div>
</section>

<section class="sheet sheet--inside">
  <div class="column column--about">
    <h2 class="column-title">About</h2>
    <div class="body-copy">
      <p>Harlow Care Group is proud to usher in a new era in long-term care - Harlow Senior Living. Harlow Senior Living was developed as a response to innumerable requests from our clients for assistance locating suitable homes or facilities when in-home care is no longer appropriate. Now, your care can remain with the best!</p>
    </div>
    <div class="photo photo--life" role="img" aria-label="Photo of two smiling senior men">
      <div class="photo__caption"><small>It's a great</small><span>life</span></div>
    </div>
    <div class="body-copy second">
      <p>Harlow Senior Living Seaview is a brand new state of the art home located in Seaview at 214 Coral Bay Drive in the Palm Ridge area. Up to 22 “neighbors” enjoy this 11,000 square feet home with 19 fully-furnished private rooms with private bathrooms. Room sizes range from 152 sq ft to 225 sq ft. Each has a flat screen television, electric bed(s), desk, chair, dressers, artwork, built-in closet system with mirrored doors, independent air conditioner, and ceiling fan.</p>
    </div>
  </div>

  <div class="column column--services">
    <svg class="services-swoosh" viewBox="0 0 213 170" preserveAspectRatio="none" aria-hidden="true">
      <path d="M0,0 C40,30 120,45 213,48 L213,170 L0,170 Z" fill="var(--teal-mid)"/>
      <path d="M0,12 C40,42 120,58 213,60 L213,170 L0,170 Z" fill="var(--teal-light)"/>
    </svg>
    <h2 class="column-title">Services</h2>
    <div class="body-copy">
      <p>Harlow Senior Living is a unique care concept, designed around a social model which encourages “neighbors” to be as independent as possible, actively participate in life here, and interact with their fellow neighbors.</p>
      <p>Here, you’ll maintain purpose in life while having personal care assistance as needed, activities, exercise, transportation, and companionship. Professional staff will be in residence 24 hours a day. This is a very special home, offering you a loving and nurturing life experience.</p>
      <p>Stay busy doing what you love here! Participate in as many activities as you like and discover life anew. Keep up your favorite hobbies or take up new ones.</p>
      <p>Harlow Senior Living is a home where neighbors are actively engaged, individuality is encouraged, and life has purpose. It’s a home!</p>
      <p><strong>Make it your home, today!</strong></p>
    </div>
  </div>

  <div class="column column--fees">
    <h2 class="column-title">Monthly Fee Includes:</h2>
    <ul class="fee-box">
      <li>3 Daily Meals + Snacks</li>
      <li>Activities</li>
      <li>Laundry</li>
      <li>Housekeeping</li>
      <li>Utilities</li>
      <li>Accommodations</li>
      <li>Medication Management</li>
      <li>Care Planning</li>
      <li>Regular Nursing Visits</li>
      <li>Access to Staff 24/7</li>
    </ul>
    <h3 class="care-heading">Lifestyle Support</h3>
    <p class="care-text">For neighbors who are relatively independent but might benefit from lifestyle support, with assistance as needed, medication management, access to staff 24/7, and regular nursing visits.</p>
    <h3 class="care-heading">Personal Care</h3>
    <p class="care-text">Hands-on care: Daily bathing, dressing, toileting, incontinence care, grooming, assistance with ambulation, transfers, range of motion exercises, verbal cueing, medication management, &amp; feeding.</p>
    <div class="photo photo--family" role="img" aria-label="Photo of a senior woman with a caregiver">
      <div class="photo__caption"><small>We're</small><span>family</span></div>
    </div>
  </div>
</section>

</body>
</html>
```